Promotion for Local Garage - KLM Motorworks offering 10% off

We are after an A5 Colour Leaflet to promote our business KLM Motorworks.

KLM Motorworks is a local garage and we are about to launch a flyer campaign in the local area.

Services we provide:
Servicing, Repairs, Diagnostics, Clutches, Brakes, Exhaust for all makes and models of cars and vans.

10% discount for anyone who brings in this flyer with them.

Company contact details below:
Telephone 0151 3846172
Website www.klmmotorworks-example.co.uk

Address
Unit 4 Hollin Workshops,
Brackwell Lane,
Fenwick Ind Estate,
Ellesmere Port,
CH64 9QP

Our Logo is attached

Target Market(s)

Local Residents and businesses

Industry/Entity Type

Auto Repair

Requirements
Must have
• Services we provide:
• Servicing, Repairs, Diagnostics, Clutches, Brakes, Exhaust for all makes and models of cars and vans.
• 10% discount for anyone who brings in this flyer with them.
• Company contact details below:
• Telephone 0151 3846172
• Website www.klmmotorworks-example.co.uk
• Address
• Unit 4 Hollin Workshops,
• Brackwell Lane,
• Fenwick Ind Estate,
• Ellesmere Port,
• CH64 9QP

```html
<!DOCTYPE html>
<html lang="en">
<head>
<meta charset="utf-8">
<title>KLM Motorworks – Services Leaflet</title>
<link rel="stylesheet" href="https://fonts.googleapis.com/css2?family=Fira+Sans+Condensed:wght@600;700;800&display=swap">
<style>
  :root{
    --red:#e31e2a;
    --red-dark:#c01722;
    --red-deep:#a8121c;
    --grey:#58585b;
    --grey-dark:#4a4a4e;
    --text:#4b4b4f;
    --white:#ffffff;
    --paper:#f4f4f4;
  }
  *{margin:0;padding:0;box-sizing:border-box}
  html,body{width:926px;height:1200px;overflow:hidden;background:var(--paper)}
  .leaflet{position:relative;width:926px;height:1200px;overflow:hidden;background:var(--white);
    font-family:"Fira Sans Condensed","Arial Narrow",sans-serif}
  .leaflet__art{position:absolute;left:0;top:0;width:926px;height:1200px}
  .services__title{position:absolute;left:55px;top:646px;font-size:40px;font-weight:800;color:var(--red);
    line-height:1;letter-spacing:-0.3px}
  .services__list{position:absolute;left:55px;top:700px;list-style:none}
  .services__item{display:flex;align-items:center;height:44px;font-size:34px;font-weight:800;color:var(--text);
    line-height:1;letter-spacing:0.2px}
  .services__tick{width:40px;height:30px;margin-right:16px;flex:none}
  .services__item--cont{padding-left:56px}
  .brand{position:absolute;left:436px;top:736px;font-size:36px;font-weight:700;color:var(--red);line-height:1}
  .offer__headline{position:absolute;left:420px;top:798px;width:370px;text-align:center;font-size:42px;
    font-weight:800;color:var(--white);line-height:56px}
  .offer__terms{position:absolute;left:540px;top:857px;width:300px;font-size:15px;font-weight:700;
    color:var(--white);line-height:20px;text-align:center}
  .contact__line{position:absolute;left:65px;top:1031px;font-size:30px;font-weight:800;color:var(--white);
    line-height:1;white-space:nowrap;letter-spacing:-0.2px}
  .address{position:absolute;left:65px;top:1108px;font-size:24px;font-weight:700;color:#f1f1f1;line-height:31px}
</style>
</head>
<body>
<div class="leaflet">
  <svg class="leaflet__art" viewBox="0 0 946 1336" preserveAspectRatio="none" aria-hidden="false">
    <defs>
      <linearGradient id="workshopTone" x1="0" y1="0" x2="0" y2="1">
        <stop offset="0" stop-color="#d9d9d7"/>
        <stop offset="0.45" stop-color="#a9abad"/>
        <stop offset="1" stop-color="#5b5d60"/>
      </linearGradient>
      <linearGradient id="oilTone" x1="0" y1="0" x2="1" y2="1">
        <stop offset="0" stop-color="#e6e1d2"/><stop offset="1" stop-color="#7c7447"/>
      </linearGradient>
      <linearGradient id="mechanicTone" x1="0" y1="0" x2="1" y2="1">
        <stop offset="0" stop-color="#3b4150"/><stop offset="1" stop-color="#a9a7a2"/>
      </linearGradient>
      <linearGradient id="engineTone" x1="0" y1="0" x2="1" y2="1">
        <stop offset="0" stop-color="#7a7c80"/><stop offset="1" stop-color="#2c2d31"/>
      </linearGradient>
      <clipPath id="clipOil"><rect x="728" y="34" width="240" height="182" rx="14"/></clipPath>
      <clipPath id="clipMech"><rect x="728" y="230" width="240" height="182" rx="14"/></clipPath>
      <clipPath id="clipEngine"><rect x="728" y="426" width="240" height="180" rx="14"/></clipPath>
    </defs>

    <g role="img" aria-label="Photo of a silver estate car raised on a blue lift in a garage workshop with a stack of tyres in front">
      <rect x="0" y="0" width="946" height="720" fill="url(#workshopTone)"/>
    </g>

    <!-- red diagonal panels -->
    <polygon points="0,258 350,650 330,700 0,523" fill="var(--red)"/>
    <polygon points="0,380 330,690 0,470" fill="var(--red-dark)"/>
    <polygon points="560,600 640,540 946,596 946,808" fill="var(--red)"/>
    <polygon points="700,600 946,640 946,808" fill="var(--red-dark)"/>
    <polygon points="250,640 330,700 420,640" fill="var(--red)"/>
    <polygon points="0,523 325,695 632,538 946,808 946,1336 0,1336" fill="var(--white)"/>

    <!-- side photos -->
    <g role="img" aria-label="Photo of engine oil being poured into an engine">
      <rect x="728" y="34" width="240" height="182" rx="14" fill="url(#oilTone)" clip-path="url(#clipOil)"/>
      <rect x="728" y="34" width="240" height="182" rx="14" fill="none" stroke="var(--red)" stroke-width="6"/>
    </g>
    <g role="img" aria-label="Photo of a mechanic using a diagnostic tool under an open bonnet">
      <rect x="728" y="230" width="240" height="182" rx="14" fill="url(#mechanicTone)" clip-path="url(#clipMech)"/>
      <rect x="728" y="230" width="240" height="182" rx="14" fill="none" stroke="var(--red)" stroke-width="6"/>
    </g>
    <g role="img" aria-label="Close-up photo of a car engine and alternator">
      <rect x="728" y="426" width="240" height="180" rx="14" fill="url(#engineTone)" clip-path="url(#clipEngine)"/>
      <rect x="728" y="426" width="240" height="180" rx="14" fill="none" stroke="var(--red)" stroke-width="6"/>
    </g>

    <!-- discount banner -->
    <polygon points="399,886 800,886 819,953 420,953" fill="var(--red)"/>
    <polygon points="539,953 844,953 864,1008 558,1008" fill="var(--grey)"/>
    <polygon points="809,886 845,886 868,940 832,940" fill="var(--grey)"/>
    <polygon points="846,915 870,915 890,965 866,965" fill="var(--red)"/>

    <!-- contact bands -->
    <polygon points="0,1150 830,1150 854,1221 0,1221" fill="var(--red)"/>
    <polygon points="0,1233 840,1233 862,1336 0,1336" fill="var(--grey)"/>
    <polygon points="830,1163 870,1163 896,1238 856,1238" fill="var(--grey-dark)"/>
    <polygon points="800,1208 840,1208 866,1283 826,1283" fill="var(--red-dark)"/>
  </svg>

  <h2 class="services__title">SERVICES WE PROVIDE:</h2>
  <ul class="services__list">
    <li class="services__item"><svg class="services__tick" viewBox="0 0 40 30"><polyline points="4,15 15,25 36,5" fill="none" stroke="var(--red)" stroke-width="6" stroke-linecap="round" stroke-linejoin="round"/></svg>SERVICING</li>
    <li class="services__item"><svg class="services__tick" viewBox="0 0 40 30"><polyline points="4,15 15,25 36,5" fill="none" stroke="var(--red)" stroke-width="6" stroke-linecap="round" stroke-linejoin="round"/></svg>REPAIRS</li>
    <li class="services__item"><svg class="services__tick" viewBox="0 0 40 30"><polyline points="4,15 15,25 36,5" fill="none" stroke="var(--red)" stroke-width="6" stroke-linecap="round" stroke-linejoin="round"/></svg>DIAGNOSTICS</li>
    <li class="services__item"><svg class="services__tick" viewBox="0 0 40 30"><polyline points="4,15 15,25 36,5" fill="none" stroke="var(--red)" stroke-width="6" stroke-linecap="round" stroke-linejoin="round"/></svg>CLUTCHES</li>
    <li class="services__item"><svg class="services__tick" viewBox="0 0 40 30"><polyline points="4,15 15,25 36,5" fill="none" stroke="var(--red)" stroke-width="6" stroke-linecap="round" stroke-linejoin="round"/></svg>BRAKES</li>
    <li class="services__item"><svg class="services__tick" viewBox="0 0 40 30"><polyline points="4,15 15,25 36,5" fill="none" stroke="var(--red)" stroke-width="6" stroke-linecap="round" stroke-linejoin="round"/></svg>EXHAUST FOR ALL MAKES</li>
    <li class="services__item services__item--cont">AND MODELS OF CARS AND VANS.</li>
  </ul>

  <div class="brand">KLM Motorworks</div>

  <div class="offer__headline">10% DISCOUNT</div>
  <p class="offer__terms">FOR ANYONE WHO BRINGS IN<br>THIS FLYER WITH THEM.</p>

  <p class="contact__line">PH: 0151 3846172 | WWW.KLMMOTORWORKS-EXAMPLE.CO.UK</p>
  <address class="address" style="font-style:normal">ADDRESS : UNIT 4 HOLLIN WORKSHOPS,&nbsp; BRACKWELL LANE,<br>FENWICK IND ESTATE, ELLESMERE PORT, CH64 9QP</address>
</div>
</body>
</html>
```